Telecommunications/Power civil contractor needs business card design

Were a new telecommunications/power underground civil contractor that is looking for a new business card design. Our company colours are silver or grey and orange. Feel free to use the white background logo or the black background logo.

Target Market(s)

Local contractors, utility companies, private sector mining/energy companies, developers.

Industry/Entity Type

Telecommunications

Contact Information for Business Card

Each card will need the following info:
Persons name:
Title:
E-mail:
Phone number:
Shop Address:
Mailing Address:

Requirements
Must have
• Each card will need the following info:
• Persons name:
• Title:
• E-mail:
• Phone number:
• Shop Address:
• Mailing Address:

```html
<!DOCTYPE html>
<html lang="en">
<head>
<meta charset="utf-8">
<title>Ridgeway Civil Works Inc — Business Card</title>
<link rel="stylesheet" href="https://fonts.googleapis.com/css2?family=Open+Sans:wght@400;600;700&display=swap">
<style>
  :root {
    --backdrop: #4a4440;
    --card: #141414;
    --card-edge: #1e1e1e;
    --orange: #f26522;
    --silver: #a6a6a6;
    --white: #f2f2f2;
  }
  * { margin: 0; padding: 0; box-sizing: border-box; }
  html, body {
    width: 1200px; height: 844px; overflow: hidden;
    background: var(--backdrop);
    font-family: "Open Sans", Arial, sans-serif;
  }
  .stage {
    position: relative; width: 1200px; height: 844px;
    display: flex; align-items: center; justify-content: center; gap: 60px;
  }
  .card {
    position: relative;
    width: 530px; height: 303px;
    background: var(--card);
    border: 1px solid var(--card-edge);
    box-shadow: 0 14px 30px rgba(0,0,0,.45);
  }
  .brand {
    display: flex; align-items: center; gap: 12px;
  }
  .brand-dot {
    width: 34px; height: 34px; border-radius: 50%;
    border: 3px solid var(--orange);
    flex: none;
  }
  .brand-name {
    color: var(--orange);
    font-weight: 700;
    font-size: 22px;
    line-height: 1.1;
    letter-spacing: .5px;
    text-transform: uppercase;
  }
  /* front side */
  .card-front .brand { position: absolute; left: 34px; top: 40px; }
  .holder { position: absolute; left: 34px; top: 168px; }
  .holder-name { font-size: 17px; font-weight: 600; color: var(--silver); }
  .holder-name .first { color: var(--orange); }
  .holder-title { font-size: 12.5px; color: var(--white); margin-top: 1px; }
  .address-label { font-size: 14px; font-weight: 600; color: var(--orange); }
  .address-line { font-size: 12.5px; color: var(--white); line-height: 1.3; }
  .shop { margin-top: 18px; }
  .contact {
    position: absolute; right: 30px; top: 116px; text-align: right;
  }
  .contact-row {
    display: flex; align-items: center; justify-content: flex-end; gap: 6px;
    font-size: 12.5px; color: var(--white); line-height: 1.6;
  }
  .contact-row svg { width: 10px; height: 10px; fill: var(--orange); flex: none; }
  .mailing { margin-top: 12px; }
  /* back side */
  .card-back { display: flex; align-items: center; justify-content: center; }
  .card-back .brand-name { font-size: 28px; }
  .card-back .brand-dot { width: 44px; height: 44px; }
</style>
</head>
<body>
<main class="stage">
  <section class="card card-front" aria-label="Business card front">
    <div class="brand">
      <span class="brand-dot"></span>
      <span class="brand-name">Ridgeway<br>Civil Works Inc</span>
    </div>

    <div class="holder">
      <p class="holder-name"><span class="first">Daniel</span> Moreau</p>
      <p class="holder-title">Managing Director</p>
      <div class="shop">
        <p class="address-label">Shop Address:</p>
        <p class="address-line">12345, Address Goes Here</p>
        <p class="address-line">Country Name, 123456</p>
      </div>
    </div>

    <div class="contact">
      <p class="contact-row">(044)-555-0182
        <svg viewBox="0 0 10 10"><path d="M2 0.5 3.6 2.6 2.7 3.6C3.3 4.9 4.9 6.6 6.3 7.2L7.3 6.3 9.5 7.9 8.6 9.5C4.5 9.3 0.7 5.5 0.5 1.4Z"/></svg>
      </p>
      <p class="contact-row">info@ridgewaycivil.com
        <svg viewBox="0 0 10 10"><path d="M0 2h10v6H0z M0 2l5 3.5L10 2" fill="var(--orange)" stroke="#141414" stroke-width=".8"/></svg>
      </p>
      <div class="mailing">
        <p class="address-label">Mailing Address:</p>
        <p class="address-line">12345, Address Goes Here</p>
        <p class="address-line">Country Name, 123456</p>
      </div>
    </div>
  </section>

  <section class="card card-back" aria-label="Business card back">
    <div class="brand">
      <span class="brand-dot"></span>
      <span class="brand-name">Ridgeway<br>Civil Works Inc</span>
    </div>
  </section>
</main>
</body>
</html>
```